"Corporal Birch" is a brand of gummied aids

Corporal Birch is a brand of service men gummies that help our heroes with anxiety, Irritability and hostility brought on by a condition known as PTSD.

I have uploaded example symbols that can be use to discribe the following
Caffeine-Free, No GMO, Sugar Free, Vegan,
Gluten Free, No THC, etc...

Looking for a label for an 8 or 10oz glass jar. The label needs to allow some view at the bottom of the jar to show the gummies.

My vision, and I welcome your, is a
silhouette of various service people saluting a, or various flags.

Each gummy is 15mg 60 count
Updates

I've decided to change the band name on the label. The project is a brand of Gummy aids for PTSD sufferers. The New Name: Valor Bites Target: All first responder service people wanting relief with no THC side affects.

Target Market(s)

All service people, Military, Police, Fire fighters, Medics, Nurses, Doctors, First Responders, etc... (Male and Females)

Font styles to use
Serif
Sans Serif

Requirements
Must have
• Correction: The service people don't have to be saluting a flag.
Note. My uploads are examples only.
Should not have
• Cartoons

```html
<!DOCTYPE html>
<html lang="en">
<head>
<meta charset="utf-8">
<title>Corporal Birch Gummies – Jar Label</title>
<link rel="stylesheet" href="https://fonts.googleapis.com/css2?family=Montserrat:wght@300;400;600&family=Roboto+Condensed:wght@400;700&display=swap">
<style>
  :root {
    --page: #f4f5f5;
    --paper: #ffffff;
    --teal: #1fae9c;
    --teal-light: #4ccbb9;
    --teal-dark: #12907f;
    --orange: #ec8a3f;
    --ink: #2b2f33;
    --soft: #d9e6e3;
  }
  * { box-sizing: border-box; margin: 0; padding: 0; }
  html, body { width: 1200px; height: 980px; overflow: hidden; background: var(--page); }
  .label {
    position: absolute; left: 90px; top: 160px; width: 1020px; height: 660px;
    display: flex; box-shadow: 0 2px 14px rgba(0,0,0,.08);
  }

  /* Side panel */
  .side-panel {
    width: 250px; background: var(--paper); padding: 26px 22px;
    font-family: "Roboto Condensed", sans-serif; color: var(--ink);
    display: flex; flex-direction: column; gap: 18px;
  }
  .badge-grid { display: grid; grid-template-columns: 1fr 1fr; gap: 22px 10px; }
  .badge { display: flex; flex-direction: column; align-items: center; gap: 5px;
    font-size: 9px; text-transform: uppercase; text-align: center; line-height: 1.15; }
  .badge-dot { width: 22px; height: 22px; border-radius: 50%; background: var(--soft); }
  .badge-dot.accent { background: var(--orange); opacity: .8; }
  .directions-box { height: 76px; background: var(--orange); border-radius: 4px; }
  .warning { font-size: 11px; line-height: 1.45; }
  .disclaimer { font-size: 10px; line-height: 1.35; border: 2px solid #35506a; padding: 5px 7px; }
  .storage { font-size: 10px; font-weight: 700; text-transform: uppercase; line-height: 1.5; }

  /* Front panel */
  .front-panel { flex: 1; display: flex; flex-direction: column; }
  .brand-band { height: 150px; background: var(--paper); display: flex; align-items: center; justify-content: center; gap: 12px; }
  .brand-name { font-family: "Montserrat", sans-serif; font-weight: 600; font-size: 50px; color: var(--orange); letter-spacing: .5px; }
  .brand-dot { width: 16px; height: 16px; border-radius: 50%; background: var(--teal); }
  .teal-panel {
    flex: 1; background: linear-gradient(100deg, var(--teal-light) 0%, var(--teal) 55%, var(--teal-light) 100%);
    display: flex; flex-direction: column; align-items: center; padding-top: 30px;
    font-family: "Montserrat", sans-serif; color: #fff;
  }
  .product-type { font-weight: 300; font-size: 60px; letter-spacing: 10px; }
  .salute-art { margin-top: 18px; width: 340px; height: 250px; }
  .claims { display: flex; margin-top: 22px; }
  .claim { font-size: 16px; letter-spacing: 1.5px; text-align: center; line-height: 1.4;
    padding: 4px 14px; border-left: 1.5px solid rgba(255,255,255,.85); }
  .claim:first-child { border-left: none; }
  .count-row { display: flex; align-items: stretch; margin-top: 22px; }
  .count { width: 100px; height: 100px; background: var(--orange); font-weight: 300; font-size: 60px;
    display: flex; align-items: center; justify-content: center; }
  .count-text { padding: 14px 0 0 14px; font-size: 16px; letter-spacing: 1.5px; }
  .count-text .rule { width: 230px; height: 1.5px; background: #fff; margin: 10px 0 14px; }
</style>
</head>
<body>
<div class="label">
  <aside class="side-panel">
    <div class="badge-grid">
      <div class="badge"><span class="badge-dot accent"></span>No Peanuts</div>
      <div class="badge"><span class="badge-dot"></span>Packaged in the USA</div>
      <div class="badge"><span class="badge-dot accent"></span>No Milk</div>
      <div class="badge"><span class="badge-dot"></span>Vegan Friendly</div>
      <div class="badge"><span class="badge-dot accent"></span>No Preservatives</div>
      <div class="badge"><span class="badge-dot"></span>Manufactured in a GMP Facility</div>
    </div>
    <div class="directions-box"></div>
    <p class="warning">Do not exceed suggested dosage. If your child has a medical condition, please consult a physician. Not recommended for children under two. Do not use if seal is broken or missing. Store at room temperature. Do not expose to heat. Color will darken over time.</p>
    <p class="warning">Contains no peanuts or soy. The facility that makes this product handles soy.</p>
    <p class="disclaimer">These statements have not been evaluated by the Food and Drug Administration. This product is not intended to diagnose, treat, cure or prevent any disease.</p>
    <p class="storage">Do not use if closure is broken.<br>Store at room temperature.</p>
  </aside>

  <section class="front-panel">
    <header class="brand-band">
      <span class="brand-name">Corporal Birch</span>
      <span class="brand-dot"></span>
    </header>
    <div class="teal-panel">
      <h1 class="product-type">GUMMIES</h1>
      <svg class="salute-art" role="img" aria-label="Row of saluting service member silhouettes growing in height, shading from dark teal to white" viewBox="0 0 340 250">
        <defs>
          <linearGradient id="salute-fade" x1="0" x2="1" y1="0" y2="0">
            <stop offset="0" stop-color="#2f6d68"/>
            <stop offset="1" stop-color="#f4f7f6"/>
          </linearGradient>
        </defs>
        <polygon points="0,250 0,150 340,0 340,250" fill="url(#salute-fade)" opacity=".85"/>
      </svg>
      <div class="claims">
        <div class="claim">100%<br>VEGAN</div>
        <div class="claim">GLUTEN<br>FREE</div>
        <div class="claim">NON<br>GMO</div>
        <div class="claim">CAFFEINE<br>FREE</div>
        <div class="claim">SUGAR<br>FREE</div>
      </div>
      <div class="count-row">
        <div class="count">60</div>
        <div class="count-text">
          <div>GUMMIES</div>
          <div class="rule"></div>
          <div>DIETARY SUPPLEMENT</div>
        </div>
      </div>
    </div>
  </section>
</div>
</body>
</html>
```